Breezeway Comfort business cards design

Need a business card design for a Heating and Air Conditioning business. I need these items included.
Business name: Breezeway Comfort
Owner: Marcus Tollefsen
License # 2874590
Phone number # 555-382-4071
Email: breezewaycomfortair@mailvista.example
Sales
Service
Installation
Maintenance

Heating and Air Conditioning

Requirements
Must have
• Company name , license number , phone number , email

```html
<!DOCTYPE html>
<html lang="en">
<head>
<meta charset="utf-8">
<title>Breezeway Comfort – Business Card</title>
<link rel="stylesheet" href="https://fonts.googleapis.com/css2?family=Michroma&family=Saira:wght@600;700&display=swap">
<style>
  :root {
    --page: #ffffff;
    --card: #ffffff;
    --frame: #3a3a3a;
    --ink: #333333;
    --label: #666666;
    --blue: #0a3ca8;
    --orange: #f58a33;
    --red: #ec4136;
    --coral: #f06a3b;
  }
  * { margin: 0; padding: 0; box-sizing: border-box; }
  html, body { width: 1200px; height: 1200px; overflow: hidden; background: var(--page); }
  body { position: relative; font-family: "Saira", sans-serif; color: var(--ink); }

  .card {
    position: absolute; left: 180px; width: 840px; height: 480px;
    background: var(--card); border: 1.5px solid var(--frame); overflow: hidden;
  }
  .card--front { top: 72px; }
  .card--back { top: 648px; }
  .card-decor { position: absolute; inset: 0; width: 100%; height: 100%; }

  .side-label {
    position: absolute; left: 0; width: 1200px; text-align: center;
    font-family: "Saira", sans-serif; font-weight: 600; font-size: 20px; color: var(--label);
  }

  .owner {
    position: absolute; right: 46px; top: 56px; text-align: right;
    border-left: 7px solid var(--blue); padding-left: 10px;
  }
  .owner-name { font-weight: 700; font-size: 29px; line-height: 1; color: var(--ink); }
  .owner-role { font-weight: 700; font-size: 15px; line-height: 1.1; color: var(--ink); }

  .brand {
    position: absolute; display: flex; align-items: center;
  }
  .brand--front { left: 150px; top: 150px; gap: 24px; }
  .brand--back { left: 0; right: 0; top: 150px; flex-direction: column; gap: 18px; }
  .brand-dot { border-radius: 50%; background: var(--orange); flex: none; }
  .brand--front .brand-dot { width: 110px; height: 110px; }
  .brand--back .brand-dot { width: 96px; height: 96px; }
  .brand-name {
    font-family: "Michroma", sans-serif; font-weight: 400; color: var(--blue);
    text-transform: uppercase; line-height: 1.15;
  }
  .brand--front .brand-name { font-size: 38px; }
  .brand--back .brand-name { font-size: 32px; text-align: center; }

  .contact {
    position: absolute; left: 0; right: 0; top: 300px; text-align: center;
    font-weight: 700; font-size: 19px; line-height: 28px; color: var(--ink);
  }
  .services {
    position: absolute; left: 126px; top: 412px; display: flex; align-items: center;
    font-weight: 700; font-size: 21px; color: var(--ink);
  }
  .services li { list-style: none; padding: 0 12px; line-height: 38px; }
  .services li:first-child { padding-left: 0; }
  .services li + li { border-left: 3px solid var(--coral); }
</style>
</head>
<body>

<section class="card card--front" aria-label="Business card front">
  <svg class="card-decor" viewBox="0 0 840 480" aria-hidden="true">
    <defs>
      <linearGradient id="cornerWarm" x1="1" y1="0" x2="0" y2="1">
        <stop offset="0" stop-color="#f58a33"/>
        <stop offset="1" stop-color="#ec3b36"/>
      </linearGradient>
      <linearGradient id="cornerWarmLow" x1="0" y1="1" x2="1" y2="0">
        <stop offset="0" stop-color="#f58a33"/>
        <stop offset="1" stop-color="#ec4a36"/>
      </linearGradient>
    </defs>
    <polygon points="0,0 190,0 0,174" fill="url(#cornerWarm)"/>
    <polygon points="140,68 184,68 0,230 0,192" fill="var(--blue)"/>
    <polygon points="840,282 840,320 744,406 698,406" fill="var(--blue)"/>
    <polygon points="840,342 840,480 690,480" fill="url(#cornerWarmLow)"/>
  </svg>

  <div class="owner">
    <div class="owner-name">Marcus Tollefsen</div>
    <div class="owner-role">Owner</div>
  </div>

  <div class="brand brand--front">
    <span class="brand-dot"></span>
    <span class="brand-name">Breezeway<br>Comfort</span>
  </div>

  <div class="contact">
    <p>License # 2874590</p>
    <p>Phone number # 555-382-4071</p>
    <p>Email: breezewaycomfortair@mailvista.example</p>
  </div>

  <ul class="services">
    <li>Sales</li>
    <li>Service</li>
    <li>Installation</li>
    <li>Maintenance</li>
  </ul>
</section>
<p class="side-label" style="top:598px;">front</p>

<section class="card card--back" aria-label="Business card back">
  <div class="brand brand--back">
    <span class="brand-dot"></span>
    <span class="brand-name">Breezeway<br>Comfort</span>
  </div>
</section>
<p class="side-label" style="top:1144px;">back</p>

</body>
</html>
```